Indian Lunch Delivery company needs a google ad banner for advertising its offering

We are a Kolkata, India based startup delivering lunch to office buildings in the city. We only serve set meals (vegetarian and non-vegetarian). Minimum order quantity is 5 boxes. The name of the brand is Verdopan (Thali=platter). Our USP-
We cook fresh
Trans-fat free
No emulsifiers, preservatives or artificial colorings used.
Importantly, we are a value for money brand. To be precise our meals costs just .99 c.
Target Market(s)
Young professionals
Industry/Entity Type
It Company
Font styles to use
Sans Serif
Requirements
Must have
- Home made food feel to it
Nice to have
- Lots of colours

```html
<!DOCTYPE html>
<html lang="en">
<head>
<meta charset="utf-8">
<title>Verdopan Lunch Banner</title>
<link rel="stylesheet" href="https://fonts.googleapis.com/css2?family=Jost:wght@400;500&display=swap">
<style>
  :root {
    --coral: #ee7862;
    --coral-deep: #e2654f;
    --slate: #636363;
    --slate-dark: #555555;
    --ink: #454545;
    --paper: #f4f4f4;
    --page: #eeeeee;
    --white: #ffffff;
  }
  html, body {
    margin: 0;
    width: 1200px;
    height: 1200px;
    overflow: hidden;
    background: var(--page);
    font-family: "Jost", sans-serif;
  }
  .banner {
    position: absolute;
    left: 40px;
    top: 492px;
    width: 1120px;
    height: 215px;
    background: var(--white);
    box-shadow: 0 2px 6px rgba(0,0,0,0.12);
  }
  .message-panel {
    position: absolute;
    left: 0; top: 0;
    width: 557px; height: 215px;
    background: linear-gradient(180deg, #f7f7f7 0%, #e9e9e9 55%, #f6f6f6 100%);
  }
  .ribbon {
    position: absolute;
    left: 44px; top: 0;
    width: 180px; height: 202px;
  }
  .ribbon-text {
    position: absolute;
    left: 44px;
    width: 180px;
    text-align: center;
    color: var(--white);
    line-height: 1;
  }
  .ribbon-fresh { top: 22px; font-size: 29px; font-weight: 400; line-height: 28px; }
  .ribbon-transfat { top: 96px; font-size: 24px; letter-spacing: -0.5px; }
  .ribbon-free { top: 118px; font-size: 54px; }
  .usp-list {
    position: absolute;
    left: 258px; top: 28px;
    margin: 0; padding: 0;
    list-style: none;
  }
  .usp-list li {
    position: relative;
    padding-left: 24px;
    font-size: 28px;
    line-height: 34.5px;
    color: var(--ink);
  }
  .usp-list li::before {
    content: "";
    position: absolute;
    left: 0; top: 13px;
    width: 10px; height: 10px;
    border-radius: 50%;
    background: var(--coral);
  }
  .price-pill {
    position: absolute;
    left: 260px; top: 147px;
    width: 264px; height: 44px;
    box-sizing: border-box;
    border: 3px solid var(--coral);
    border-radius: 24px;
    background: var(--slate-dark);
    color: var(--white);
    font-size: 21px;
    line-height: 38px;
    text-align: center;
    box-shadow: 0 4px 4px rgba(0,0,0,0.12);
  }
  .coral-stripe {
    position: absolute;
    left: 557px; top: 0;
    width: 9px; height: 215px;
    background: var(--coral);
  }
  .food-photo {
    position: absolute;
    top: 0; height: 215px;
  }
  .food-photo.curry-plate {
    left: 566px; width: 189px;
    background: radial-gradient(circle at 50% 70%, #c0492e 0%, #d98a5c 30%, #eadccb 60%, #b9965e 100%);
  }
  .food-photo.thali-spread {
    left: 945px; width: 175px;
    background: radial-gradient(circle at 45% 60%, #b8a244 0%, #a77a2c 40%, #d7c29a 70%, #6e4a22 100%);
  }
  .brand-panel {
    position: absolute;
    left: 760px; top: 0;
    width: 180px; height: 215px;
    background: var(--coral);
  }
  .brand-badge {
    position: absolute;
    left: 16px; top: 39px;
    width: 148px; height: 148px;
    box-sizing: border-box;
    border-radius: 50%;
    background: var(--slate);
    border: 4px solid var(--white);
    display: flex;
    align-items: center;
    justify-content: center;
  }
  .brand-name {
    color: var(--white);
    font-size: 19px;
    font-weight: 500;
    letter-spacing: 0.5px;
  }
</style>
</head>
<body>
  <div class="banner">
    <div class="message-panel"></div>

    <svg class="ribbon" viewBox="0 0 180 202" aria-hidden="true">
      <polygon points="0,186 90,202 180,186 180,170 0,170" fill="#5a5a5a"/>
      <polygon points="0,88 180,88 180,176 90,192 0,176" fill="var(--coral)"/>
      <rect x="0" y="0" width="180" height="88" fill="var(--slate)"/>
    </svg>
    <div class="ribbon-text ribbon-fresh">FRESHLY<br>COOKED</div>
    <div class="ribbon-text ribbon-transfat">TRANS-FAT</div>
    <div class="ribbon-text ribbon-free">FREE</div>

    <ul class="usp-list">
      <li>No Emulsifiers</li>
      <li>Preservatives</li>
      <li>Artificial colorings</li>
    </ul>
    <div class="price-pill">MEALS FOR JUST .99 C</div>

    <div class="coral-stripe"></div>
    <div class="food-photo curry-plate" role="img" aria-label="Photo of a home-style meal with curry, rice, naan and lime"></div>

    <div class="brand-panel">
      <div class="brand-badge"><span class="brand-name">VERDOPAN</span></div>
    </div>

    <div class="food-photo thali-spread" role="img" aria-label="Photo of a brass thali platter with small bowls of dal and curries"></div>
  </div>
</body>
</html>
```